Animal Eye Clinic needs a Business card

We are a new veterinary ophthalmology practice (Tessaly Animal Eye Care) and we need a business card designed. We only see animal eyes - we are not a regular veterinary clinic. We already have a logo. We are looking for a professional, good looking business card to hand out to our clients. We are looking for something simple but professional and contemporary. Our logo is likely the only picture/graphic that needs to be on the card.
Updates

Contact Information for Business Card

Marisol Dunkley, BSc, DVM, MSc, DipACVO
Veterinary Ophthalmologist

Phone: 250.418.3097
Email: tessalyanimaleyecare@mailbrook.net
Website: tessalyanimaleyecare.net
Address: 1840 Pellworth Rd
Kelowna, BC, V4T 8M3

Colors

Designer to choose colors to be used in the design.

Requirements
Must have
• Our logo (attached)

```html
<!DOCTYPE html>
<html lang="en">
<head>
<meta charset="utf-8">
<title>Tessaly Animal Eye Care – Business Card</title>
<link rel="stylesheet" href="https://fonts.googleapis.com/css2?family=Roboto:wght@400;500;700&display=swap">
<style>
  :root {
    --teal: #0096a9;
    --white: #ffffff;
    --ink-grey: #6b6b6b;
    --rule-grey: #7a7a7a;
    --faint: #eef2f4;
    --backdrop: #4a4a4a;
  }
  * { box-sizing: border-box; margin: 0; padding: 0; }
  html, body {
    width: 1200px; height: 1200px; overflow: hidden;
    background: var(--backdrop);
    font-family: "Roboto", Arial, sans-serif;
  }
  .stage {
    width: 1200px; height: 1200px;
    display: flex; flex-direction: column; align-items: center; justify-content: center;
    gap: 60px;
  }
  .card {
    position: relative;
    width: 820px; height: 469px;
    border-radius: 22px;
    overflow: hidden;
  }
  /* Back side */
  .card--back { background: var(--teal); color: var(--white); }
  .brand {
    display: flex; align-items: center; gap: 18px;
  }
  .brand__mark {
    width: 64px; height: 64px; border-radius: 50%;
    flex: none;
  }
  .brand__name {
    font-weight: 500; letter-spacing: 0.5px; white-space: nowrap;
  }
  .card--back .brand {
    position: absolute; left: 50%; top: 175px; transform: translateX(-50%);
  }
  .card--back .brand__mark { background: var(--white); }
  .card--back .brand__name { font-size: 40px; color: var(--white); }
  .card--back .website {
    position: absolute; left: 0; right: 0; bottom: 44px;
    text-align: center; font-size: 18px; font-weight: 500;
  }
  /* Front side */
  .card--front { background: var(--white); }
  .decor-circle {
    position: absolute; right: -90px; bottom: -120px;
    width: 440px; height: 440px; border-radius: 50%;
    background: var(--faint);
  }
  .holder {
    position: absolute; left: 48px; top: 52px; right: 40px;
  }
  .holder__name {
    color: var(--teal); font-weight: 700; font-size: 36px; letter-spacing: 0.3px;
  }
  .holder__title {
    color: var(--ink-grey); font-size: 22px; margin-top: 4px; padding-left: 210px;
  }
  .card--front .brand {
    position: absolute; left: 48px; top: 250px;
  }
  .card--front .brand__mark { width: 48px; height: 48px; background: var(--teal); }
  .card--front .brand__name { font-size: 25px; color: var(--teal); }
  .divider {
    position: absolute; left: 430px; top: 220px; width: 1px; height: 170px;
    background: var(--rule-grey);
  }
  .contact {
    position: absolute; left: 456px; top: 222px;
    color: var(--ink-grey); font-size: 18px; line-height: 1.35;
  }
  .contact__address { margin-bottom: 12px; }
  .contact__row { display: flex; align-items: center; gap: 10px; margin-top: 3px; }
  .contact__icon { width: 16px; height: 16px; flex: none; }
</style>
</head>
<body>
<main class="stage">
  <section class="card card--back">
    <div class="brand">
      <span class="brand__mark"></span>
      <span class="brand__name">Tessaly Animal Eye Care</span>
    </div>
    <p class="website">tessalyanimaleyecare.net</p>
  </section>

  <section class="card card--front">
    <div class="decor-circle"></div>
    <header class="holder">
      <h1 class="holder__name">Marisol Dunkley, BSc, DVM, MSc, DipACVO</h1>
      <p class="holder__title">Veterinary Ophthalmologist</p>
    </header>
    <div class="brand">
      <span class="brand__mark"></span>
      <span class="brand__name">Tessaly Animal Eye Care</span>
    </div>
    <div class="divider"></div>
    <address class="contact" style="font-style:normal">
      <p class="contact__address">1840 Pellworth Rd<br>Kelowna, BC, V4T 8M3</p>
      <p class="contact__row">
        <svg class="contact__icon" viewBox="0 0 24 24"><path fill="#0096a9" d="M6.6 10.8a15.1 15.1 0 0 0 6.6 6.6l2.2-2.2c.3-.3.7-.4 1-.2 1.1.4 2.3.6 3.6.6.6 0 1 .4 1 1V20c0 .6-.4 1-1 1A17 17 0 0 1 3 4c0-.6.4-1 1-1h3.5c.6 0 1 .4 1 1 0 1.3.2 2.5.6 3.6.1.3 0 .7-.2 1z"/></svg>
        250.418.3097
      </p>
      <p class="contact__row">
        <svg class="contact__icon" viewBox="0 0 24 24"><rect x="2" y="5" width="20" height="14" rx="1" fill="#0096a9"/><path d="M3 6l9 7 9-7" fill="none" stroke="#fff" stroke-width="1.6"/></svg>
        tessalyanimaleyecare@mailbrook.net
      </p>
      <p class="contact__row">
        <svg class="contact__icon" viewBox="0 0 24 24" fill="none" stroke="#0096a9" stroke-width="1.8"><circle cx="12" cy="12" r="9.5"/><ellipse cx="12" cy="12" rx="4" ry="9.5"/><path d="M2.5 12h19M4 7h16M4 17h16"/></svg>
        tessalyanimaleyecare.net
      </p>
    </address>
  </section>
</main>
</body>
</html>
```